Construction Company

Design a clutter free business card, it can be double-sided utilizing the logo for BNX Ltd simple with all relevant contact information.

Please also a letterhead design to function for the purposes of invoicing, all mail requirements, with header to be distinctive while the footer ties page together and incorporates all necessary information.

For now, please use generic / dummy text and when a winner is selected, I will disclose the contact information.

Hi Designers! Please read the updated brief which includes the design of a business card and letterhead. Thank you!

```html
<!DOCTYPE html>
<html lang="en">
<head>
<meta charset="utf-8">
<title>BNX Ltd – Letterhead</title>
<link rel="stylesheet" href="https://fonts.googleapis.com/css2?family=Source+Sans+3:wght@400;600&display=swap">
<style>
  :root {
    --ink: #171b1c;
    --paper: #ffffff;
    --slate: #e1e2e4;
    --ghost: #c9cacc;
  }
  html, body {
    margin: 0;
    padding: 0;
    overflow: hidden;
    background: var(--paper);
  }
  .letterhead {
    position: relative;
    width: 849px;
    height: 1200px;
    overflow: hidden;
    background: var(--paper);
    font-family: "Source Sans 3", sans-serif;
    color: var(--ink);
  }
  .diagonal-panel {
    position: absolute;
    inset: 0;
    width: 849px;
    height: 1200px;
  }
  .edge-bar {
    position: absolute;
    left: 13px;
    top: 8px;
    width: 19px;
    height: 150px;
    background: var(--ink);
  }
  .header-brand {
    position: absolute;
    left: 546px;
    top: 40px;
    width: 212px;
    text-align: center;
  }
  .header-brand .brand-name {
    display: block;
    font-size: 58px;
    font-weight: 600;
    line-height: 1;
    letter-spacing: -1px;
  }
  .header-brand .brand-tagline {
    display: block;
    margin-top: 42px;
    font-size: 13.5px;
    font-weight: 400;
    letter-spacing: 0.1px;
  }
  .background-name {
    position: absolute;
    left: 0;
    top: 535px;
    width: 849px;
    text-align: center;
    font-size: 128px;
    font-weight: 600;
    line-height: 1;
    letter-spacing: -3px;
    color: var(--ghost);
    opacity: 0.85;
  }
  .footer-block {
    position: absolute;
    left: 570px;
    top: 1072px;
    width: 160px;
  }
  .footer-block .footer-name-row {
    display: flex;
    align-items: flex-end;
    height: 36px;
  }
  .footer-block .footer-name {
    font-size: 30px;
    font-weight: 600;
    line-height: 1;
    letter-spacing: -0.5px;
  }
  .footer-block .footer-band {
    flex: 1;
    height: 18px;
    margin-left: 4px;
    margin-bottom: 2px;
    background: var(--ink);
  }
  .footer-block .footer-line {
    margin: 0 0 0 9px;
    font-size: 13px;
    font-weight: 400;
    line-height: 16px;
  }
</style>
</head>
<body>
  <main class="letterhead">
    <svg class="diagonal-panel" viewBox="0 0 849 1200" aria-hidden="true">
      <polygon points="849,5 849,1200 277,1200" fill="var(--slate)"/>
    </svg>

    <div class="edge-bar"></div>

    <header class="header-brand">
      <span class="brand-name">BNX Ltd</span>
      <span class="brand-tagline">CONSTRUCTION COMPANY</span>
    </header>

    <div class="background-name" aria-hidden="true">BNX Ltd</div>

    <footer class="footer-block">
      <div class="footer-name-row">
        <span class="footer-name">BNX Ltd</span>
        <span class="footer-band"></span>
      </div>
      <p class="footer-line">CONSTRUCTION COMPANY</p>
      <p class="footer-line">Address</p>
    </footer>
  </main>
</body>
</html>
```